E-Waste Recycling Company Business Card

New Electronic Recycling Company based in Long Island, New York called "Greenwire Recovery" We take outdated computers, components, electrical wire, circuit breakers, ink cartridges, etc. We look mostly for donated items that we recycle for our customers but will pay for large quantities from businesses. The design should reflect that we are environmentally friendly and our unique 7Q Obliteration process that ensures all personal data is wiped clean off hard drives. Please use our attached logo
Industry/Entity Type
Electrical

```html
<!DOCTYPE html>
<html lang="en">
<head>
<meta charset="utf-8">
<title>Greenwire Recovery — Business Card</title>
<link rel="stylesheet" href="https://fonts.googleapis.com/css2?family=Didact+Gothic&family=Montserrat:wght@700&display=swap">
<style>
  :root {
    --backdrop: #e7e9e6;
    --card-white: #f4f4f4;
    --green-deep: #1f7a24;
    --green-mid: #3fa437;
    --green-light: #5cc04f;
    --green-glow: #52b847;
    --ink: #3b3b3b;
    --ink-soft: #555555;
    --white: #ffffff;
  }
  * { box-sizing: border-box; margin: 0; padding: 0; }
  html, body { width: 1200px; height: 900px; overflow: hidden; }
  body {
    background: var(--backdrop);
    font-family: "Didact Gothic", "Century Gothic", sans-serif;
    position: relative;
  }
  .card {
    position: absolute;
    left: 280px;
    width: 640px;
    height: 366px;
    overflow: hidden;
    box-shadow: 0 10px 28px rgba(0,0,0,0.18);
  }
  .card--back {
    top: 52px;
    background: radial-gradient(ellipse at 50% 40%, var(--green-glow) 0%, var(--green-mid) 45%, var(--green-deep) 100%);
    display: flex;
    align-items: center;
    justify-content: center;
  }
  .brand {
    display: flex;
    align-items: center;
    gap: 14px;
  }
  .brand__dot {
    width: 24px; height: 24px; border-radius: 50%;
    background: var(--white);
  }
  .brand__name {
    font-size: 38px;
    color: var(--white);
    white-space: nowrap;
  }
  .card--front {
    top: 482px;
    background: var(--card-white);
  }
  .wave { position: absolute; inset: 0; }
  .holder {
    position: absolute; left: 40px; top: 40px;
  }
  .holder__name {
    font-family: "Montserrat", sans-serif;
    font-weight: 700;
    font-size: 15px;
    letter-spacing: 1px;
    color: var(--ink);
  }
  .holder__role {
    font-size: 13px;
    color: var(--green-mid);
    margin-top: 6px;
  }
  .front-brand {
    position: absolute; left: 300px; top: 40px;
    display: flex; align-items: center; gap: 8px;
  }
  .front-brand__dot {
    width: 14px; height: 14px; border-radius: 50%;
    background: var(--green-mid);
  }
  .front-brand__name {
    font-size: 20px;
    color: var(--green-mid);
    white-space: nowrap;
  }
  .contacts {
    position: absolute; left: 262px; top: 108px;
    list-style: none;
  }
  .contacts li {
    display: flex; align-items: center; gap: 14px;
    font-size: 14px; color: var(--ink-soft);
    height: 26px;
    white-space: nowrap;
  }
  .contacts li.no-icon { padding-left: 28px; }
  .contacts svg { width: 14px; height: 14px; flex: none; }
  .website {
    position: absolute; left: 220px; top: 318px;
    font-size: 22px; color: var(--white);
    letter-spacing: 0.5px;
  }
</style>
</head>
<body>
  <section class="card card--back" aria-label="Card back">
    <div class="brand">
      <span class="brand__dot"></span>
      <span class="brand__name">Greenwire Recovery</span>
    </div>
  </section>

  <section class="card card--front" aria-label="Card front">
    <svg class="wave" viewBox="0 0 640 366" preserveAspectRatio="none" aria-hidden="true">
      <path d="M0,150 C90,250 260,270 640,300 L640,366 L0,366 Z" fill="var(--green-deep)"/>
      <path d="M0,168 C100,262 280,280 640,312 L640,366 L0,366 Z" fill="var(--green-light)"/>
      <path d="M0,210 C130,290 330,300 640,330 L640,366 L0,366 Z" fill="var(--green-mid)"/>
    </svg>

    <div class="holder">
      <p class="holder__name">OWEN BALCOMBE, GSC</p>
      <p class="holder__role">President</p>
    </div>

    <div class="front-brand">
      <span class="front-brand__dot"></span>
      <span class="front-brand__name">Greenwire Recovery</span>
    </div>

    <ul class="contacts">
      <li class="no-icon">418 Harrow Lane Eastfield, BC, V2K 5R3</li>
      <li>
        <svg viewBox="0 0 16 16" aria-hidden="true"><path d="M2 6c0-2 3-3 6-3s6 1 6 3l-2 1-1-2H5L4 7z M4 8h8l1 5H3z" fill="var(--green-mid)"/></svg>
        250.555.0147
      </li>
      <li>
        <svg viewBox="0 0 16 16" aria-hidden="true"><rect x="4" y="2" width="8" height="4" fill="var(--green-mid)"/><rect x="2" y="6" width="12" height="6" rx="1" fill="var(--green-mid)"/><rect x="5" y="10" width="6" height="4" fill="var(--white)" stroke="var(--green-mid)"/></svg>
        250.555.0163
      </li>
      <li>
        <svg viewBox="0 0 16 16" aria-hidden="true"><rect x="1.5" y="3.5" width="13" height="9" fill="none" stroke="var(--green-mid)" stroke-width="1.5"/><path d="M2 4l6 5 6-5" fill="none" stroke="var(--green-mid)" stroke-width="1.5"/></svg>
        owen.balcombe@email.com
      </li>
    </ul>

    <p class="website">www.website.com</p>
  </section>
</body>
</html>
```